Travel Company is looking for a STAND OUT Business Card

I need a unique Business Card that will truly stand out. Nothing too busy. Simple is good, right? Not looking for a standard design either. No cookie cutter layout. We are a Travel Company that works more with Companies than Travelers. I had an idea to focus and emphasis on the 2 logo a bit more. This is not necessary, however thought it would look interesting. I am just looking for something interesting and a bit different. Does't have to completely off the wall crazy, just not your run of the mill business card.

Target Market(s)

Hoteliers, Resort Management, Call Centers, Executives, Travelers, Families, Businesses

Industry/Entity Type

Hospitality

Contact Information for Business Card

President/CEO - Marcus T Bellamy (title not necessary if design doesn't allow for it)
contact - (407) 555-0186
email - mbellamy@wayfarenow.example
address - 4812 Quillmore Ave #164
Orlando, FL 32804
website - www.wayfarenow.example

Font styles to use
Serif
Other font styles liked:
• Avenir Next LT Pro BOLD

Requirements
Must have
• simple look and design. Unique design
Nice to have
• I attached the 2 logo separate from the main logo. This can be used separately from the Main Logo, together with the main logo or as main logo. I included the logo font. Use it or not, designers choice.
Should not have
• cookie cutter design. Little use of red other than the logo

```html
<!DOCTYPE html>
<html lang="en">
<head>
<meta charset="utf-8">
<title>Wayfare Now – Business Card</title>
<link rel="stylesheet" href="https://fonts.googleapis.com/css2?family=Cabin:wght@400;700&display=swap">
<style>
  :root {
    --brand-red: #ff0000;
    --ink: #111111;
    --paper: #ffffff;
    --backdrop: #e6e6e6;
  }
  * { margin: 0; padding: 0; box-sizing: border-box; }
  html, body {
    width: 1200px;
    height: 1087px;
    overflow: hidden;
    background: var(--backdrop);
    font-family: "Cabin", "Gill Sans", sans-serif;
  }
  .canvas { position: relative; width: 1200px; height: 1087px; }
  .card {
    position: absolute;
    left: 281px;
    width: 657px;
    height: 375px;
  }
  .card--front { top: 125px; background: var(--paper); }
  .card--back { top: 542px; background: var(--brand-red); }

  .name-tag { position: absolute; left: 0; top: 48px; width: 242px; height: 89px; }
  .name-tag svg { position: absolute; inset: 0; }
  .name-tag__name {
    position: absolute; left: 25px; top: 14px;
    color: var(--brand-red); font-size: 25px; font-weight: 400;
  }
  .name-tag__title {
    position: absolute; left: 25px; top: 49px;
    color: var(--paper); font-size: 20px;
  }

  .wordmark {
    font-weight: 700;
    letter-spacing: -0.5px;
    white-space: nowrap;
  }
  .card--front .wordmark {
    position: absolute; left: 32px; top: 226px;
    font-size: 46px; color: var(--ink);
  }
  .contact {
    position: absolute; left: 28px; top: 300px;
    font-size: 17.5px; line-height: 28px; color: var(--ink);
  }
  .contact .accent { color: var(--brand-red); }

  .brand-circle {
    position: absolute; left: 400px; top: 60px;
    width: 220px; height: 220px;
    border: 14px solid var(--brand-red);
    border-radius: 50%;
  }

  .card--back .lockup {
    position: absolute; left: 0; right: 0; top: 150px;
    display: flex; align-items: center; justify-content: center; gap: 14px;
  }
  .card--back .wordmark { font-size: 52px; color: var(--ink); }
  .lockup__dot {
    width: 30px; height: 30px; border-radius: 50%; background: var(--paper);
  }
</style>
</head>
<body>
<main class="canvas">
  <section class="card card--front" aria-label="Business card front">
    <div class="name-tag">
      <svg width="242" height="89" viewBox="0 0 242 89" aria-hidden="true">
        <polygon points="0,0 208,0 242,44.5 208,89 0,89" fill="#111111"/>
      </svg>
      <p class="name-tag__name">Marcus T Bellamy</p>
      <p class="name-tag__title">President/CEO</p>
    </div>

    <div class="brand-circle" aria-hidden="true"></div>

    <p class="wordmark">Wayfare Now</p>

    <address class="contact" style="font-style:normal">
      <p>4812 Quillmore Ave #164, Orlando, FL 32804</p>
      <p>(407) 555-0186 | mbellamy@<span class="accent">wayfarenow</span>.example | www.<span class="accent">wayfarenow</span>.example</p>
    </address>
  </section>

  <section class="card card--back" aria-label="Business card back">
    <div class="lockup">
      <span class="lockup__dot" aria-hidden="true"></span>
      <p class="wordmark">Wayfare Now</p>
    </div>
  </section>
</main>
</body>
</html>
```